Need Business Card for our Real Estate Business with Sales Executive's Picture

PANTONE 484 C ( RED)

PANTONE 2766 C ( BLUE

Industry/Entity Type

Real Estate

Contact Information for Business Card

Name, Mobile, email, & picture of Person
Agency Phone, address, Web address

Requirements
Must have
• Our Logo Colours, Agent Picture,

```html
<!DOCTYPE html>
<html lang="en">
<head>
<meta charset="utf-8">
<title>Dunewood Real Estate – Business Card</title>
<link rel="stylesheet" href="https://fonts.googleapis.com/css2?family=Questrial&display=swap">
<style>
  :root {
    --backdrop: #d9d9d9;
    --navy: #131a4a;
    --brand-red: #8f2a2f;
    --card-white: #f3f3f1;
    --ink: #2b2b2b;
    --ink-soft: #4a4a4a;
  }
  * { box-sizing: border-box; margin: 0; padding: 0; }
  html, body {
    width: 1200px; height: 1000px; overflow: hidden;
    background: var(--backdrop);
    font-family: "Questrial", "Helvetica Neue", Arial, sans-serif;
  }
  .sheet {
    position: relative; width: 1200px; height: 1000px;
    display: flex; flex-direction: column; align-items: center; justify-content: center; gap: 60px;
  }
  .card {
    position: relative; width: 600px; height: 343px;
    box-shadow: 0 6px 18px rgba(0,0,0,0.15);
  }
  /* Front */
  .card-front {
    background: var(--navy);
    display: flex; align-items: center; justify-content: center;
  }
  .brand {
    display: flex; flex-direction: column; align-items: center; gap: 6px;
    color: #ffffff;
  }
  .brand-name {
    font-size: 40px; letter-spacing: 6px; line-height: 1;
  }
  .brand-sub {
    font-size: 11px; letter-spacing: 4px;
  }
  .brand-rule {
    width: 170px; height: 1px; background: #ffffff;
  }
  /* Back */
  .card-back { background: var(--card-white); }
  .agent {
    position: absolute; left: 72px; top: 58px; width: 200px;
    display: flex; flex-direction: column; align-items: center;
  }
  .agent-portrait { width: 180px; height: 180px; display: block; }
  .agent-name {
    margin-top: 18px; font-size: 22px; letter-spacing: 1.5px; color: var(--ink);
    white-space: nowrap;
  }
  .contact {
    position: absolute; left: 370px; top: 60px; height: 206px;
    border-left: 1.5px solid var(--ink);
    padding-left: 16px;
    display: flex; flex-direction: column; justify-content: space-between;
  }
  .contact-item { display: flex; flex-direction: column; gap: 2px; }
  .contact-label { font-size: 13px; color: var(--ink); letter-spacing: 0.5px; }
  .contact-value { font-size: 10.5px; color: var(--ink-soft); letter-spacing: 0.6px; }
</style>
</head>
<body>
<main class="sheet">
  <section class="card card-front" aria-label="Card front">
    <div class="brand">
      <span class="brand-name">DUNEWOOD</span>
      <span class="brand-rule"></span>
      <span class="brand-sub">REAL ESTATE</span>
    </div>
  </section>

  <section class="card card-back" aria-label="Card back">
    <div class="agent">
      <svg class="agent-portrait" viewBox="0 0 180 180">
        <defs>
          <linearGradient id="ring" x1="0" y1="0" x2="1" y2="1">
            <stop offset="0" stop-color="#1e2462"/>
            <stop offset="1" stop-color="#a23a3c"/>
          </linearGradient>
          <linearGradient id="photo-tone" x1="0" y1="0" x2="0" y2="1">
            <stop offset="0" stop-color="#dcdad4"/>
            <stop offset="0.6" stop-color="#b8a89a"/>
            <stop offset="1" stop-color="#26305e"/>
          </linearGradient>
        </defs>
        <circle cx="90" cy="90" r="90" fill="url(#ring)"/>
        <circle cx="90" cy="90" r="78" fill="url(#photo-tone)" role="img" aria-label="Portrait photo of the sales executive in a navy suit"/>
      </svg>
      <p class="agent-name">Marko Jelavic</p>
    </div>

    <div class="contact">
      <div class="contact-item">
        <span class="contact-label">Mobile Phone</span>
        <span class="contact-value">+00 555 0142</span>
      </div>
      <div class="contact-item">
        <span class="contact-label">Email</span>
        <span class="contact-value">marko@dunewoodhomes.com</span>
      </div>
      <div class="contact-item">
        <span class="contact-label">Web</span>
        <span class="contact-value">www.dunewoodhomes.com</span>
      </div>
      <div class="contact-item">
        <span class="contact-label">Address</span>
      </div>
      <div class="contact-item">
        <span class="contact-label">Phone</span>
        <span class="contact-value">555-0187</span>
      </div>
    </div>
  </section>
</main>
</body>
</html>
```